For Sale Poster Design

We need a beautiful and tropical looking FOR SALE poster for our speed boat.

Poster format need to be 297x420mm / 300dpi
PSD with all layers.

The photos from the boat can be downloaded here: www.korvado.nl/photos.zip

Target Market(s)

Tourists, expats

Requirements
Must have
• The poster need to have the following text:

Speed Boat Sale

This beautiful full glass fiber speedboat (location Lombok, Indonesia) is perfect for tropical conditions: island transfer, diving, wake boarding, fishing, private charters and leisure activities.

The newly bought 2x 200 HP TORUMI 4 Stroke (2013) will give you an enormous power on the water with maximum speed of 40 Knot / 74 Km/hour. This will bring you from Lombok to Bali in just 50 minutes and only few minutes long from the famous tropical Gili islands.

The speedboat also has the comfort of a small cabin with skylight, sun controlled ventilation system, a small bed, a toilet and a fridge. There are 16 seats in the open section of the boat. The boat is equipped with modern brand-new GPS, Sonar and an FM / AM Radio system.

This speedboat was built in 2011 and is meticulously maintained to the highest standard. It comes with a captain and boatman.

Specs:
Overall length: 11 Meter 36 feet.
Built year: 2011, Bali
Engines: 2x 200 HP TORUMI 4 Stroke (Bought 2013)
Capacity: Max. 16 People (Incl. Crew)
Max speed: 40 Knot / 74 Km/hour
GPS / Sonar: Pelcorn RM-42TX
Tankage: 300 Liter
Lighting: LED / Halogen

Price 99.000 USD
Nice to have
• Big FOR SALE banner on the poster

```html
<!DOCTYPE html>
<html lang="en">
<head>
<meta charset="utf-8">
<title>Speed Boat For Sale Poster</title>
<link href="https://fonts.googleapis.com/css2?family=Anton&family=Arimo:wght@400;700&family=Nunito:wght@900&display=swap" rel="stylesheet">
<style>
  :root {
    --page: #ffffff;
    --orange: #e84e1b;
    --brown: #3d2a1e;
    --frame: #7a5f4a;
    --text: #3a2a20;
    --sky-top: #5b8fd0;
    --sky-low: #bfe0f3;
    --sea: #2fb7c0;
    --sand: #e9e3d6;
    --pebble: #b9ad97;
    --seat: #d8c19b;
    --outline: #ffffff;
  }
  html, body { margin: 0; padding: 0; width: 1200px; height: 1029px; overflow: hidden; background: var(--page); }
  .poster { position: absolute; left: 275px; top: 25px; width: 692px; height: 992px; overflow: hidden; }
  .scene-beach { position: absolute; left: 0; top: 0; width: 692px; height: 420px;
    background: linear-gradient(180deg, var(--sky-top) 0%, var(--sky-low) 38%, var(--sea) 62%, #8fd3cf 80%, var(--sand) 100%); }
  .scene-shore { position: absolute; left: 0; top: 380px; width: 692px; height: 612px;
    background: linear-gradient(180deg, #6fc4cf 0%, var(--sand) 25%, #d7cfbf 60%, var(--pebble) 100%); }
  .overlay { position: absolute; left: 0; top: 0; }
  .photo { position: absolute; border-radius: 50%; box-sizing: border-box; border: 8px solid var(--frame); }
  .photo-helm { left: 0; top: 265px; width: 224px; height: 224px; background: radial-gradient(circle at 50% 55%, #f4f3ef 0%, #dcdad4 60%, var(--seat) 100%); }
  .photo-cabin { left: 186px; top: 255px; width: 134px; height: 134px; border-width: 6px; background: radial-gradient(circle at 50% 70%, #c9b08a 0%, #ecebe6 60%); }
  .photo-deck { left: 122px; top: 368px; width: 294px; height: 294px; background: radial-gradient(circle at 50% 45%, #f2f2ef 0%, #e3e1db 45%, var(--seat) 85%); }

  .titles text { paint-order: stroke; stroke: var(--outline); stroke-linejoin: round; }
  .price { font-family: "Nunito", sans-serif; font-weight: 900; font-size: 76px; fill: var(--orange); stroke-width: 8px; }
  .headline { font-family: "Anton", sans-serif; font-size: 80px; fill: var(--brown); stroke-width: 7px; }
  .banner { font-family: "Nunito", sans-serif; font-weight: 900; font-size: 84px; fill: var(--orange); stroke-width: 8px; }

  .copy p { position: absolute; margin: 0; font-family: "Arimo", sans-serif; color: var(--text); font-size: 11px; line-height: 15px; white-space: nowrap; }
  .copy-use { left: 395px; top: 390px; width: 300px; text-align: center; }
  .copy-engine { left: 425px; top: 465px; width: 260px; text-align: center; }
  .copy-comfort { right: 47px; top: 584px; text-align: right; }
  .copy-care { right: 70px; top: 689px; text-align: right; }
  .specs { position: absolute; left: 232px; top: 730px; width: 340px; margin: 0; font-family: "Arimo", sans-serif; color: var(--text); font-size: 13px; line-height: 17px; text-align: center; }
  .specs-title { display: block; margin-bottom: 17px; }
</style>
</head>
<body>
  <main class="poster">
    <div class="scene-shore" role="img" aria-label="Photo of a white coral pebble beach"></div>
    <div class="scene-beach" role="img" aria-label="Photo of a tropical beach with palm trees, rocks and the speed boat on turquoise water"></div>
    <svg class="overlay" width="692" height="992" viewBox="0 0 692 992" aria-hidden="true">
      <path d="M14 380 C 20 200, 230 110, 360 110 C 500 110, 690 190, 692 330 L 692 560 C 640 760, 470 900, 360 985 C 250 890, 60 720, 14 520 Z" fill="rgba(255,255,255,0.55)"/>
      <path d="M14 380 C 20 200, 230 110, 360 110 C 500 110, 690 190, 692 330" fill="none" stroke="rgba(255,255,255,0.8)" stroke-width="3"/>
    </svg>
    <div class="photo photo-helm" role="img" aria-label="Photo of the helm with two captain seats"></div>
    <div class="photo photo-cabin" role="img" aria-label="Photo of the small cabin with bed"></div>
    <div class="photo photo-deck" role="img" aria-label="Photo of the open deck with cushioned benches"></div>

    <div class="copy">
      <p class="copy-use">This beautiful full glass fiber speed boat (location<br>Lombok, Indonesia) is perfect for tropical conditions.<br>Island transfer, diving, wake boarding, fishing,<br>private charters and leisure features.</p>
      <p class="copy-engine">The new (2013) bought 2x 200 HP TORUMI 4<br>Stroke will give you an enormous power on the<br>water with maximum speed of 40 Knot / 74<br>Km/hour and will bring you within only 50<br>minutes from Lombok to Bali and within<br>minute distance from all famous tropical Gili<br>islands.</p>
      <p class="copy-comfort">The speed boat also has the comfort of a small<br>cabin with skylight, sun controlled ventilation<br>system, a small bed, a toilet and a fridge. In the open<br>section of the boat are 16 seats, besides all of this is the<br>boat equipped with brand-new GPS, Sonar and an FM / AM<br>Radio system.</p>
      <p class="copy-care">This boat was built in 2011 and it was meticulously<br>maintained to the highest standard.</p>
    </div>

    <p class="specs">
      <span class="specs-title">Specs:</span>
      Overall length: 11 Meter 36 feet.<br>
      Built year: 2011, Bali<br>
      Engines: 2x 200 HP TORUMI 4 Stroke (Bought 2013)<br>
      Capacity: Max. 16 People (Incl. Crew)<br>
      Max speed: 40 Knot / 74 Km/hour<br>
      GPS / Sonar: Pelcorn RM-42TX<br>
      Tankage: 300 Liter<br>
      Lighting: LED / Halogen
    </p>

    <svg class="overlay titles" width="692" height="992" viewBox="0 0 692 992">
      <text class="price" x="34" y="77" textLength="580" lengthAdjust="spacingAndGlyphs">Price 99.000 USD</text>
      <text class="headline" x="318" y="366" textLength="368" lengthAdjust="spacingAndGlyphs">SPEED BOAT SALE</text>
      <text class="banner" x="163" y="865" text-anchor="middle" textLength="360" lengthAdjust="spacingAndGlyphs" transform="rotate(45 163 835)">FOR SALE</text>
    </svg>
  </main>
</body>
</html>
```